Upmarket building and construction company needs signage

Our building company R Brent Construction, needs signage to put up on the side of our vehicle trailers and on site fencing. We are a building company that specialises in residential construction and carpentry .

I will attach our logo and some inspirational pics for site fencing as well as what our trailer looks like .
Other details i would like on the sign are our
( email) rbrentconstruction@mailbox-example.net
(mobile ) 0493 518 264
(website ) rbrentconstruction. example.net

Target Market(s)

Home owners looking for a reliable local builder who produces good quality work. I have attached some inspirational pics.

Industry/Entity Type

Building and Construction

Colors

Designer to choose colors to be used in the design.

Requirements
Must have
• Our logo, contact information
Nice to have
• We would like the design to have elements of being Elegant, Serious, Modern, Professional, Masculine, Conservative and Upmarket.

```html
<!DOCTYPE html>
<html lang="en">
<head>
<meta charset="utf-8">
<title>R Brent Construction – signage panels</title>
<link rel="stylesheet" href="https://fonts.googleapis.com/css2?family=Jost:wght@300;400&display=swap">
<style>
  :root{
    --page:#d0d0d0;
    --slate:#6784a0;
    --navy:#35485e;
    --ink:#ffffff;
    --stripe-light:#a5a5a8;
    --stripe-dark:#6f6f72;
    --ghost-light:#8fa2b5;
    --ghost-dark:#5d6c7e;
  }
  *{margin:0;padding:0;box-sizing:border-box}
  html,body{width:1200px;height:881px;overflow:hidden;background:var(--page)}
  body{position:relative;font-family:"Jost",sans-serif;color:var(--ink);font-weight:300}

  .panel{position:absolute;width:341px;height:170px;overflow:hidden}
  .panel--slate{background:var(--slate)}
  .panel--navy{background:var(--navy)}

  .wordmark{position:absolute;font-weight:300;font-size:12px;line-height:14px;letter-spacing:1.2px;text-transform:uppercase;white-space:nowrap;display:flex;align-items:center;gap:6px}
  .wordmark__square{width:10px;height:10px;background:var(--ink);flex:none}
  .wordmark--side{font-size:9.5px;line-height:11.5px;letter-spacing:.8px;gap:4px}
  .wordmark--side .wordmark__square{width:8px;height:8px}
  .wordmark--compact{font-size:7.5px;line-height:9px;letter-spacing:.6px;gap:3px}
  .wordmark--compact .wordmark__square{width:6px;height:6px}
  .wordmark--center{left:0;right:0;justify-content:center;text-align:center}

  .contacts{position:absolute;list-style:none;font-size:7px;line-height:10.2px;letter-spacing:.2px;white-space:nowrap}
  .contacts li{display:flex;align-items:center;gap:5px}
  .contacts svg{width:5px;height:5px;flex:none}
  .contacts--large{font-size:7.4px}
  .contacts--compact{font-size:6.4px;line-height:8.6px}

  .tagline{position:absolute;left:0;right:0;text-align:center;font-size:11px;letter-spacing:.3px}

  .stripe{position:absolute;width:12px}
  .panel--slate .stripe{background:var(--stripe-light)}
  .panel--navy .stripe{background:var(--stripe-dark)}

  .statement{position:absolute;bottom:0;display:flex;align-items:flex-end}
  .statement__col{writing-mode:vertical-rl;transform:rotate(180deg);white-space:nowrap}
  .statement__col--ghost{font-size:17px;line-height:17.5px}
  .panel--slate .statement__col--ghost{color:var(--ghost-light)}
  .panel--navy .statement__col--ghost{color:var(--ghost-dark)}
  .statement__col--spaced{font-size:16px;line-height:18.5px;letter-spacing:4.6px;margin-left:2px}
</style>
</head>
<body>

<svg width="0" height="0" style="position:absolute" aria-hidden="true">
  <symbol id="i-phone" viewBox="0 0 10 10"><rect x="2.5" y="0.5" width="5" height="9" rx="0.8" fill="none" stroke="#fff" stroke-width="1"/><line x1="4" y1="8" x2="6" y2="8" stroke="#fff" stroke-width="0.8"/></symbol>
  <symbol id="i-mail" viewBox="0 0 10 10"><rect x="0.5" y="2" width="9" height="6" fill="none" stroke="#fff" stroke-width="1"/><polyline points="0.5,2 5,5.5 9.5,2" fill="none" stroke="#fff" stroke-width="1"/></symbol>
  <symbol id="i-web" viewBox="0 0 10 10"><circle cx="5" cy="5" r="4.4" fill="none" stroke="#fff" stroke-width="1"/><ellipse cx="5" cy="5" rx="2" ry="4.4" fill="none" stroke="#fff" stroke-width="0.8"/><line x1="0.6" y1="5" x2="9.4" y2="5" stroke="#fff" stroke-width="0.8"/></symbol>
</svg>

<!-- Row 1 : slate -->
<section class="panel panel--slate" style="left:76px;top:53px">
  <div class="wordmark wordmark--side" style="left:76px;top:92px"><span class="wordmark__square"></span><span>R Brent<br>Construction</span></div>
  <ul class="contacts" style="left:182px;top:89px">
    <li><svg><use href="#i-phone"/></svg>0493 518 264</li>
    <li><svg><use href="#i-mail"/></svg>rbrentconstruction@mailbox-example.net</li>
    <li><svg><use href="#i-web"/></svg>rbrentconstruction. example.net</li>
  </ul>
</section>

<section class="panel panel--slate" style="left:430px;top:53px">
  <div class="wordmark wordmark--center" style="top:64px"><span>R Brent<br>Construction</span></div>
  <p class="tagline" style="top:114px">Residential Construction &amp; Carpentry</p>
</section>

<section class="panel panel--slate" style="left:783px;top:51px">
  <span class="stripe" style="left:0;top:0;height:170px"></span>
  <span class="stripe" style="left:73px;top:0;height:170px"></span>
  <span class="stripe" style="left:147px;top:0;height:67px"></span>
  <span class="stripe" style="left:147px;top:147px;height:23px"></span>
  <span class="stripe" style="left:220px;top:0;height:67px"></span>
  <span class="stripe" style="left:220px;top:147px;height:23px"></span>
  <span class="stripe" style="left:256px;top:0;height:67px"></span>
  <span class="stripe" style="left:256px;top:147px;height:23px"></span>
  <span class="stripe" style="left:293px;top:0;height:170px"></span>
  <span class="stripe" style="left:329px;top:0;height:170px"></span>
  <div class="wordmark wordmark--compact" style="left:104px;top:104px"><span class="wordmark__square"></span><span>R Brent<br>Construction</span></div>
  <ul class="contacts contacts--compact" style="left:183px;top:100px">
    <li><svg><use href="#i-phone"/></svg>0493 518 264</li>
    <li><svg><use href="#i-mail"/></svg>rbrentconstruction@<br>mailbox-example.net</li>
    <li><svg><use href="#i-web"/></svg>rbrentconstruction. example.net</li>
  </ul>
</section>

<!-- Row 2 : slate vertical -->
<section class="panel panel--slate" style="left:76px;top:248px">
  <div class="wordmark" style="left:22px;top:34px"><span class="wordmark__square"></span><span>R Brent<br>Construction</span></div>
  <ul class="contacts contacts--large" style="left:22px;top:122px">
    <li><svg><use href="#i-phone"/></svg>0493 518 264</li>
    <li><svg><use href="#i-mail"/></svg>rbrentconstruction@<br>mailbox-example.net</li>
    <li><svg><use href="#i-web"/></svg>rbrentconstruction. example.net</li>
  </ul>
  <div class="statement" style="left:186px">
    <p class="statement__col statement__col--ghost">Residential<br>Construction<br>&amp;Carpentry</p>
    <p class="statement__col statement__col--spaced">Residential<br>Construction<br>&amp;Carpentry</p>
  </div>
</section>

<!-- Row 3 : navy -->
<section class="panel panel--navy" style="left:76px;top:457px">
  <div class="wordmark wordmark--side" style="left:76px;top:92px"><span class="wordmark__square"></span><span>R Brent<br>Construction</span></div>
  <ul class="contacts" style="left:182px;top:89px">
    <li><svg><use href="#i-phone"/></svg>0493 518 264</li>
    <li><svg><use href="#i-mail"/></svg>rbrentconstruction@mailbox-example.net</li>
    <li><svg><use href="#i-web"/></svg>rbrentconstruction. example.net</li>
  </ul>
</section>

<section class="panel panel--navy" style="left:430px;top:457px">
  <div class="wordmark wordmark--center" style="top:64px"><span>R Brent<br>Construction</span></div>
  <p class="tagline" style="top:114px">Residential Construction &amp; Carpentry</p>
</section>

<section class="panel panel--navy" style="left:783px;top:456px">
  <span class="stripe" style="left:0;top:0;height:170px"></span>
  <span class="stripe" style="left:73px;top:0;height:170px"></span>
  <span class="stripe" style="left:147px;top:0;height:67px"></span>
  <span class="stripe" style="left:147px;top:147px;height:23px"></span>
  <span class="stripe" style="left:220px;top:0;height:67px"></span>
  <span class="stripe" style="left:220px;top:147px;height:23px"></span>
  <span class="stripe" style="left:256px;top:0;height:67px"></span>
  <span class="stripe" style="left:256px;top:147px;height:23px"></span>
  <span class="stripe" style="left:293px;top:0;height:170px"></span>
  <span class="stripe" style="left:329px;top:0;height:170px"></span>
  <div class="wordmark wordmark--compact" style="left:104px;top:104px"><span class="wordmark__square"></span><span>R Brent<br>Construction</span></div>
  <ul class="contacts contacts--compact" style="left:183px;top:100px">
    <li><svg><use href="#i-phone"/></svg>0493 518 264</li>
    <li><svg><use href="#i-mail"/></svg>rbrentconstruction@<br>mailbox-example.net</li>
    <li><svg><use href="#i-web"/></svg>rbrentconstruction. example.net</li>
  </ul>
</section>

<!-- Row 4 : navy vertical -->
<section class="panel panel--navy" style="left:76px;top:652px">
  <div class="wordmark" style="left:22px;top:34px"><span class="wordmark__square"></span><span>R Brent<br>Construction</span></div>
  <ul class="contacts contacts--large" style="left:22px;top:75px">
    <li><svg><use href="#i-phone"/></svg>0493 518 264</li>
    <li><svg><use href="#i-mail"/></svg>rbrentconstruction@<br>mailbox-example.net</li>
    <li><svg><use href="#i-web"/></svg>rbrentconstruction. example.net</li>
  </ul>
  <div class="statement" style="left:186px">
    <p class="statement__col statement__col--ghost">Residential<br>Construction<br>&amp;Carpentry</p>
    <p class="statement__col statement__col--spaced">Residential<br>Construction<br>&amp;Carpentry</p>
  </div>
</section>

</body>
</html>
```